KELD, Inc. new buisness cards - brand guide included

We need new business cards. SLEAK SIMPLE FINANCE. They must include a place for NAME, TITLE, CELL, OFFICE PHONE, EMAIL. they also must include our services across the bottom. AIR, OCEAN, FTL, LTL, EXPRESS. for reference this will be being handed to some of the most prestigious shipping companies in a america.

Target Market(s)

Finance and corporate

Contact Information for Business Card

We need new business cards. SLEAK SIMPLE FINANCE. They must include a place for NAME, TITLE, CELL, OFFICE PHONE, EMAIL. they also must include our services across the bottom. AIR, OCEAN, FTL, LTL, EXPRESS.

Requirements
Must have
• We need new business cards. SLEAK SIMPLE FINANCE. They must include a place for NAME, TITLE, CELL, OFFICE PHONE, EMAIL. they also must include our services across the bottom. AIR, OCEAN, FTL, LTL, EXPRESS.
Nice to have
• USE THE COLORS AND LOGO IN THE BRAND GUIDE :)

```html
<!DOCTYPE html>
<html lang="en">
<head>
<meta charset="utf-8">
<title>KELD, Inc. Business Cards</title>
<link rel="stylesheet" href="https://fonts.googleapis.com/css2?family=Open+Sans:wght@400;600;700&display=swap">
<style>
  :root {
    --page-bg: #d9d9d9;
    --card-dark: #333333;
    --pattern-dark: #2b2b2b;
    --card-light: #ffffff;
    --ink: #2f2f2f;
    --ink-soft: #6a6a6a;
    --paper: #f4f2ee;
  }
  * { margin: 0; padding: 0; box-sizing: border-box; }
  html, body { width: 1200px; height: 901px; overflow: hidden; }
  body {
    background: var(--page-bg);
    font-family: "Open Sans", Arial, sans-serif;
    position: relative;
  }
  .card {
    position: absolute;
    width: 560px;
    height: 320px;
    box-shadow: 0 10px 30px rgba(0,0,0,0.25);
    overflow: hidden;
  }

  /* Back of card */
  .card-back { left: 80px; top: 100px; background: var(--card-dark); color: var(--paper); }
  .card-back .pattern-area {
    position: absolute; inset: 0;
    background: linear-gradient(135deg, var(--pattern-dark), var(--card-dark) 60%, var(--pattern-dark));
  }
  .card-back .brand-block {
    position: absolute; left: 0; right: 0; top: 92px;
    display: flex; flex-direction: column; align-items: center;
  }
  .brand-name {
    display: flex; align-items: center; gap: 12px;
    font-weight: 600; font-size: 46px; letter-spacing: 6px; line-height: 1;
  }
  .brand-name .brand-square { width: 14px; height: 14px; background: currentColor; }
  .services-pill {
    margin-top: 16px;
    background: var(--paper); color: var(--ink);
    font-weight: 700; font-size: 17px; letter-spacing: 1px;
    padding: 4px 22px; border-radius: 20px;
  }
  .services-list {
    position: absolute; left: 0; right: 0; bottom: 50px;
    display: flex; justify-content: center; gap: 14px;
    font-size: 22px; letter-spacing: 1px;
  }
  .services-list li { list-style: none; display: flex; align-items: center; gap: 8px; }
  .services-list li::before {
    content: ""; width: 8px; height: 8px; border-radius: 50%; background: var(--paper);
  }

  /* Front of card */
  .card-front { left: 560px; top: 480px; background: var(--card-light); color: var(--ink); }
  .card-front .frame {
    position: absolute; left: 24px; top: 24px; right: 24px; bottom: 24px;
    border: 2px solid var(--ink);
  }
  .card-front .brand-name {
    position: absolute; left: 0; right: 0; top: 58px; justify-content: center;
    color: var(--ink); font-size: 44px;
  }
  .person {
    position: absolute; right: 306px; top: 190px; text-align: right;
  }
  .person-name { font-weight: 700; font-size: 21px; letter-spacing: 0.5px; }
  .person-title { font-size: 15px; color: var(--ink-soft); margin-top: 2px; }
  .divider {
    position: absolute; left: 272px; top: 170px; width: 1px; height: 86px; background: var(--ink);
  }
  .contact-list {
    position: absolute; left: 290px; top: 170px; list-style: none;
    font-size: 15px; color: var(--ink-soft); line-height: 21px;
  }
  .contact-list li { display: flex; align-items: center; gap: 7px; }
  .contact-list svg { width: 12px; height: 12px; fill: var(--ink); flex: none; }
  .address {
    position: absolute; left: 0; right: 0; bottom: 14px; text-align: center;
  }
  .address span {
    background: var(--card-light); padding: 0 12px;
    font-size: 15px; color: var(--ink-soft); letter-spacing: 0.5px;
  }
</style>
</head>
<body>

<section class="card card-back">
  <div class="pattern-area" role="img" aria-label="Dark embossed background pattern of repeated company name tiles"></div>
  <div class="brand-block">
    <div class="brand-name"><span class="brand-square"></span>KELD</div>
    <div class="services-pill">OUR SERVICES</div>
  </div>
  <ul class="services-list">
    <li>AIR</li><li>OCEAN</li><li>FTL</li><li>LTL</li><li>EXPRESS</li>
  </ul>
</section>

<section class="card card-front">
  <div class="frame"></div>
  <div class="brand-name"><span class="brand-square"></span>KELD</div>
  <div class="person">
    <div class="person-name">DANIEL BROOKS</div>
    <div class="person-title">Managing Director</div>
  </div>
  <div class="divider"></div>
  <ul class="contact-list">
    <li><svg viewBox="0 0 12 12"><path d="M1 4c0-2 2-3 5-3s5 1 5 3l-2 1-1-1H4L3 5zM2 6h8v5H2z"/></svg>312-555 018 274</li>
    <li><svg viewBox="0 0 12 12"><path d="M3 0h6v12H3zM4 1v8h4V1z"/></svg>312-555 018 274</li>
    <li><svg viewBox="0 0 12 12"><path d="M0 2h12v8H0zM1 3l5 4 5-4z"/></svg>info@keldinc.com</li>
    <li><svg viewBox="0 0 12 12"><circle cx="6" cy="6" r="6"/></svg>www.keldinc.com</li>
  </ul>
  <div class="address"><span>Your Address, City, State, Zip 0000</span></div>
</section>

</body>
</html>
```